Outdoor group fitness training - Greta Moxley Personal Training

I want an eye catching A4 flyer that promotes my two outdoor fitness groups. I have uploaded photos of each location: Mylor and Pasadena.
The target group is existing and potential new Personal training clients - all adults. There are two morning groups at Mylor ; one evening and one morning group at Pasadena. The groups will be for up to 8 people and are for all fitness levels.I want to encourage people to come and have a go. I have also uploaded a design I have used through printhollow for a previous flyer. I would like to use the orange graphic of the two people at the bottom of this design.
Cost is $15 per person
Location and times - Brackenridge Oval Wednesdays 7.30am; Sundays 8am
Corvale High School Thursdays 6.30pm: Saturdays 8am
Updates

Thanks so much to all of you for submitting a great set of designs. it was really hard making a choice in the end, and I really appreciate the promptness and creativity that went into the designs. I will certainly keep you in mind for future jobs. Cheers and have a great day Greta Moxley

Target Market(s)

40 - 60 year old adults: cross section of professionals, tradespeople and retirees. People who will enjoy socialising while also getting fit. No extremely fit people - cross section of beginners to intermediate; males and females

Industry/Entity Type

Training

Font styles to use
Sans Serif

Colors
f78f20
9bcb3c
ecf7fb

Requirements
Must have
• Fast turnaround required - within two days
Bright and attention grabbing, engaging. Could be A4 or could be postcard size?

State cost clearly
State that first 5 people to join either group will get first session at half price

```html
<!DOCTYPE html>
<html lang="en">
<head>
<meta charset="utf-8">
<title>Greta Moxley Personal Training – Outdoor Group Fitness Flyer</title>
<link rel="stylesheet" href="https://fonts.googleapis.com/css2?family=Arimo:wght@400;700&family=Noto+Sans:wght@400&display=swap">
<style>
  :root {
    --page-bg: #e8e6e2;
    --brand-orange: #f78f20;
    --bright-orange: #f2761a;
    --brand-green: #9bcb3c;
    --headline-green: #8fe23a;
    --panel-green: rgba(88, 128, 52, 0.72);
    --panel-edge: rgba(120, 160, 70, 0.55);
    --text-white: #ffffff;
    --photo-dark: #3a2a1c;
    --photo-green: #5b7a3c;
    --photo-orange: #c8621e;
    --photo-grey: #8c8a85;
  }

  html, body {
    margin: 0;
    padding: 0;
    width: 1200px;
    height: 982px;
    overflow: hidden;
    background: var(--page-bg);
  }

  .flyer {
    position: absolute;
    left: 50px;
    top: 131px;
    width: 1100px;
    height: 720px;
    overflow: hidden;
    box-shadow: 0 6px 24px rgba(0, 0, 0, 0.25);
    font-family: "Noto Sans", Verdana, sans-serif;
    color: var(--text-white);
  }

  .running-photo {
    position: absolute;
    inset: 0;
    background:
      linear-gradient(180deg, var(--photo-dark) 0%, rgba(58, 42, 28, 0) 22%),
      linear-gradient(180deg, rgba(0,0,0,0) 86%, var(--photo-grey) 88%, var(--photo-grey) 100%),
      linear-gradient(90deg, var(--photo-green) 0%, #6f8a48 40%, #b46a2c 62%, var(--photo-orange) 80%, #9e3e16 100%);
  }

  .trainer-name {
    position: absolute;
    left: 40px;
    top: 26px;
    margin: 0;
    font-family: "Arimo", Arial, sans-serif;
    font-weight: 700;
    font-size: 56px;
    color: var(--brand-orange);
    letter-spacing: 0.5px;
  }

  .info-panel {
    position: absolute;
    left: 28px;
    top: 104px;
    width: 1040px;
    height: 530px;
    background: var(--panel-green);
    border-radius: 6px;
    box-shadow: inset 0 0 0 1px var(--panel-edge);
  }

  .intro-line {
    position: absolute;
    left: 0;
    width: 900px;
    margin: 0;
    text-align: center;
    font-size: 26px;
    white-space: pre;
  }
  .intro-line.groups { top: 40px; }
  .intro-line.welcome { top: 104px; }
  .intro-line.social { top: 168px; }

  .offer {
    position: absolute;
    left: 30px;
    top: 232px;
    width: 400px;
    margin: 0;
    text-align: center;
    font-size: 46px;
    line-height: 1.22;
    color: var(--headline-green);
  }
  .offer .highlight { color: var(--bright-orange); }

  .cost {
    position: absolute;
    left: 600px;
    top: 216px;
    margin: 0;
    font-size: 28px;
  }

  .schedule-title {
    position: absolute;
    left: 612px;
    top: 306px;
    margin: 0;
    font-size: 26px;
    font-weight: 400;
  }

  .venue {
    position: absolute;
    left: 616px;
    margin: 0;
    font-size: 20px;
    line-height: 1.25;
  }
  .venue.brackenridge { top: 370px; }
  .venue.corvale { top: 458px; }
</style>
</head>
<body>
  <article class="flyer">
    <div class="running-photo" role="img" aria-label="Photo of two people running along a waterfront path, tinted green and orange"></div>

    <h1 class="trainer-name">Greta Moxley</h1>

    <section class="info-panel">
      <p class="intro-line groups">Up to 8 people per group.   Beginners to intermediate.</p>
      <p class="intro-line welcome">Males and Females are all welcome!</p>
      <p class="intro-line social">Enjoy socialising while getting fit at the same time</p>

      <p class="offer">First <span class="highlight">5</span> people to join either group will get first session at <span class="highlight">half price!</span></p>

      <p class="cost">Cost is $15 per person</p>

      <h2 class="schedule-title">Location and time:</h2>
      <p class="venue brackenridge">Brackenridge Oval<br>Wednesdays 7.30am<br>Sundays 8am</p>
      <p class="venue corvale">Corvale High School<br>Thursdays 6.30pm Saturdays 8am</p>
    </section>
  </article>
</body>
</html>
```